Lantern Business Cards

Need business cards for my employees at my restaurant.

Needs to include:
Our Logo
Lantern Bowls & Brews
Name: Nora Pettigrew
Title : Owner
Address: 487 Mirella Ave. Lake Havasu City, AZ 86519
Web: www.lanternkestrel.com
Phone: 928-555-0147
Cell: 928-555-0192
Email: info@lanternkestrel.com

```html
<!DOCTYPE html>
<html lang="en">
<head>
<meta charset="utf-8">
<title>Lantern Bowls &amp; Brews — Business Cards</title>
<link href="https://fonts.googleapis.com/css2?family=Montserrat:wght@400;500;700&display=swap" rel="stylesheet">
<style>
  :root {
    --bg: #e6e6e8;
    --card-white: #ffffff;
    --card-black: #1c1c1d;
    --brand-red: #c01f2e;
    --ink: #1f1f1f;
  }
  * { margin: 0; padding: 0; box-sizing: border-box; }
  html, body {
    width: 1200px; height: 1108px; overflow: hidden;
    background: var(--bg);
    font-family: "Montserrat", sans-serif;
  }
  .card { position: absolute; overflow: hidden; }
  .card--front { left: 222px; top: 51px; width: 786px; height: 480px; background: var(--card-white); }
  .card--back  { left: 220px; top: 577px; width: 788px; height: 463px; background: var(--card-black); }

  .front-wave { position: absolute; left: 0; top: 0; width: 786px; height: 480px; }

  .brand { position: absolute; display: flex; flex-direction: column; align-items: center; }
  .brand__mark { border-radius: 50%; background: var(--brand-red); }
  .brand__name { font-weight: 700; color: var(--brand-red); line-height: 1; white-space: nowrap; text-align: center; }

  .card--front .brand { left: 74px; top: 152px; width: 310px; }
  .card--front .brand__mark { width: 112px; height: 112px; margin-bottom: 34px; }
  .card--front .brand__name { font-size: 20px; }

  .card--back .brand { left: 0; top: 104px; width: 788px; }
  .card--back .brand__mark { width: 150px; height: 150px; margin-bottom: 44px; }
  .card--back .brand__name { font-size: 30px; letter-spacing: 0.5px; }

  .divider { position: absolute; left: 401px; top: 147px; width: 2px; height: 232px; background: var(--brand-red); }

  .contact { position: absolute; left: 420px; top: 142px; color: var(--ink); }
  .contact__name { font-size: 29px; font-weight: 700; color: var(--brand-red); line-height: 1.2; }
  .contact__title { font-size: 17px; margin-top: 2px; }
  .contact__address { font-size: 17px; line-height: 22px; margin-top: 14px; }
  .contact__list { list-style: none; margin-top: 16px; }
  .contact__item { display: flex; align-items: center; font-size: 17px; height: 27px; }
  .contact__item svg { width: 20px; height: 20px; margin-right: 10px; fill: var(--brand-red); flex: none; }
</style>
</head>
<body>

<section class="card card--front">
  <svg class="front-wave" viewBox="0 0 786 480" aria-hidden="true">
    <path d="M0 392 C120 360 230 370 360 395 C520 425 640 470 786 418 L786 480 L0 480 Z" fill="var(--card-black)"/>
    <path d="M158 374 C330 380 480 440 600 452 C680 458 740 430 786 410 L786 420 C730 452 670 470 600 466 C470 456 330 395 158 374 Z" fill="var(--card-white)"/>
    <path d="M158 374 C320 378 470 430 600 444 C680 452 740 400 786 362 L786 404 C740 440 680 462 600 458 C470 450 330 390 158 374 Z" fill="var(--brand-red)"/>
  </svg>

  <div class="brand">
    <div class="brand__mark"></div>
    <div class="brand__name">Lantern Bowls &amp; Brews</div>
  </div>

  <div class="divider"></div>

  <div class="contact">
    <div class="contact__name">Nora Pettigrew</div>
    <div class="contact__title">Owner</div>
    <div class="contact__address">487 Mirella Ave.<br>Lake Havasu City, AZ 86519</div>
    <ul class="contact__list">
      <li class="contact__item">
        <svg viewBox="0 0 24 24"><path d="M6.6 10.8a15 15 0 0 0 6.6 6.6l2.2-2.2a1 1 0 0 1 1-.25 11.4 11.4 0 0 0 3.6.57 1 1 0 0 1 1 1V20a1 1 0 0 1-1 1A17 17 0 0 1 3 4a1 1 0 0 1 1-1h3.5a1 1 0 0 1 1 1c0 1.25.2 2.45.57 3.6a1 1 0 0 1-.25 1z"/></svg>
        928-555-0192
      </li>
      <li class="contact__item">
        <svg viewBox="0 0 24 24"><path d="M3 8c0-2 4-4 9-4s9 2 9 4v2h-5V8H8v2H3z"/><rect x="5" y="11" width="14" height="9" rx="1"/></svg>
        928-555-0147
      </li>
      <li class="contact__item">
        <svg viewBox="0 0 24 24"><path d="M2 5h20v14H2z"/><path d="M2 5l10 8 10-8" fill="none" stroke="#fff" stroke-width="2"/></svg>
        info@lanternkestrel.com
      </li>
      <li class="contact__item">
        <svg viewBox="0 0 24 24"><circle cx="12" cy="12" r="10"/><path d="M7 7c2 1 3 3 2 5s1 3 1 5M14 4c0 2 2 3 4 3M15 14c1 1 3 1 4 0" fill="none" stroke="#fff" stroke-width="1.6"/></svg>
        www.lanternkestrel.com
      </li>
    </ul>
  </div>
</section>

<section class="card card--back">
  <div class="brand">
    <div class="brand__mark"></div>
    <div class="brand__name">Lantern Bowls &amp; Brews</div>
  </div>
</section>

</body>
</html>
```